Dune Business Card Design Project

We have an existing business card. We are looking to creat a new card for the store. I have attached a my own business so you have a refference of what the current card looks like.

Phone: 1300 574 213
email: merrow@dunepanes.com.au
website: www.dunepanes.com.au
Address: (Inside Merrow Rug Hall) 418 Tolvey Rd, Pelbrook VIC 3158
Updates

This is a new business card for our store.

Industry/Entity Type

Business

Requirements
Must have
• Must look similar to the existing card

```html
<!DOCTYPE html>
<html lang="en">
<head>
<meta charset="utf-8">
<title>Dune Shutters &amp; Blinds – Business Card</title>
<link rel="stylesheet" href="https://fonts.googleapis.com/css2?family=Arimo:wght@400;700&display=swap">
<style>
  :root {
    --backdrop: #d9d9d6;
    --card: #fbfbf9;
    --band: #ebeae6;
    --ink: #2a2a2a;
    --brand-grey: #4a4a4a;
    --tagline-grey: #7a7a7a;
    --accent-red: #d7222f;
    --accent-blue: #8fd0ea;
    --accent-yellow: #d4b019;
    --card-shadow: 0 10px 28px rgba(0, 0, 0, 0.18);
  }

  * { box-sizing: border-box; margin: 0; padding: 0; }

  html, body {
    width: 1200px;
    height: 900px;
    overflow: hidden;
  }

  body {
    background: var(--backdrop);
    font-family: "Arimo", Arial, sans-serif;
    color: var(--ink);
    display: flex;
    flex-direction: column;
    align-items: center;
    justify-content: center;
    gap: 56px;
  }

  .card {
    position: relative;
    width: 600px;
    height: 366px;
    background: var(--card);
    box-shadow: var(--card-shadow);
    overflow: hidden;
  }

  .brand-name {
    display: block;
    font-weight: 400;
    color: var(--brand-grey);
    letter-spacing: 0.02em;
    line-height: 1;
  }
  .brand-tagline {
    display: block;
    font-weight: 700;
    color: var(--tagline-grey);
    line-height: 1.1;
  }

  /* Front */
  .card-front__header {
    position: absolute;
    inset: 0 0 auto 0;
    height: 150px;
  }
  .card-front .brand { position: absolute; left: 38px; top: 34px; }
  .card-front .brand-name { font-size: 66px; }
  .card-front .brand-tagline { font-size: 19px; margin-top: 4px; }

  .person {
    position: absolute;
    right: 38px;
    top: 56px;
    text-align: right;
  }
  .person__name {
    font-size: 27px;
    font-weight: 700;
    color: var(--accent-red);
    line-height: 1.1;
  }
  .person__role {
    font-size: 15px;
    color: var(--ink);
    letter-spacing: 0.03em;
    margin-top: 2px;
  }

  .card-front__band {
    position: absolute;
    inset: 150px 0 0 0;
    background: var(--band);
  }

  .accent-strip {
    position: absolute;
    left: 38px;
    top: 62px;
    width: 160px;
    height: 36px;
    border-radius: 18px;
    background: linear-gradient(90deg, var(--accent-blue), var(--accent-red), var(--accent-yellow));
    opacity: 0.55;
  }

  .contact {
    position: absolute;
    right: 38px;
    top: 30px;
    text-align: right;
    font-size: 16px;
    font-style: normal;
    line-height: 1.45;
  }
  .contact__address { margin-bottom: 30px; }
  .contact__line {
    display: flex;
    justify-content: flex-end;
    align-items: center;
    gap: 10px;
    margin-top: 6px;
  }
  .contact__badge {
    width: 21px;
    height: 21px;
    border-radius: 50%;
    background: var(--accent-red);
    color: #fff;
    font-size: 13px;
    line-height: 21px;
    text-align: center;
    flex: none;
  }

  /* Back */
  .card-back .brand { position: absolute; left: 150px; top: 110px; }
  .card-back .brand-name { font-size: 86px; }
  .card-back .brand-tagline { font-size: 23px; margin-top: 6px; }

  .website {
    position: absolute;
    left: 130px;
    top: 262px;
    font-size: 17px;
    display: flex;
    align-items: baseline;
    gap: 18px;
  }
  .website__marker {
    color: var(--accent-red);
    font-size: 13px;
    letter-spacing: -0.05em;
  }
</style>
</head>
<body>

  <section class="card card-front" aria-label="Business card front">
    <div class="card-front__header">
      <div class="brand">
        <span class="brand-name">dune</span>
        <span class="brand-tagline">Shutters &amp; Blinds</span>
      </div>
      <div class="person">
        <p class="person__name">Alan Crosby</p>
        <p class="person__role">DIRECTOR</p>
      </div>
    </div>

    <div class="card-front__band">
      <div class="accent-strip" role="img" aria-label="Decorative accent in blue, red and yellow"></div>

      <address class="contact">
        <p class="contact__address">Inside Merrow Rug Hall<br>418 Tolvey Rd, Pelbrook VIC 3158</p>
        <p class="contact__line"><span>1300 574 213</span><span class="contact__badge">t</span></p>
        <p class="contact__line"><span>merrow@dunepanes.com.au</span><span class="contact__badge">e</span></p>
      </address>
    </div>
  </section>

  <section class="card card-back" aria-label="Business card back">
    <div class="brand">
      <span class="brand-name">dune</span>
      <span class="brand-tagline">Shutters &amp; Blinds</span>
    </div>
    <p class="website"><span class="website__marker">&gt;&gt;</span><span>www.dunepanes.com.au</span></p>
  </section>

</body>
</html>
```